Brightbay Business Card Design

Our company is called Brightbay. We manufacture confectionary snacks & frozen novelties. Our initial product portfolio includes frozen ice lollies/popsicles & stick ice cream bars.

We require a business card design.

Please use the attached Logo.

Please use an orange, brown, yellow colour code. You may choose any combination of the 3 or include all three. The logo however must remain orange.

Target Market(s)

Business card will be targeted at distributors of our products such as supermarket procurement managers, convenience store owners, wholesale distributors and merchandising agents.

Industry/Entity Type

Business

Requirements
Must have
• Calvin Obeng_Director/ P.O.Box Dunmore 5172, Accra, Ghana / m: 00233(0)507318924/ e: calvin.obeng@mailvora.co.uk

```html
<!DOCTYPE html>
<html lang="en">
<head>
<meta charset="utf-8">
<title>Brightbay Business Card</title>
<link rel="stylesheet" href="https://fonts.googleapis.com/css2?family=PT+Sans:wght@400;700&display=swap">
<style>
  :root {
    --page-bg: #e4e2de;
    --card-light: #f7f4f0;
    --card-mid: #e2d8cd;
    --card-shade: #cdbfb1;
    --brown-dark: #5e3a12;
    --brown-mid: #9a7550;
    --brown-light: #e2cdb5;
    --stripe-orange: #f06a1e;
    --stripe-yellow: #f7d000;
    --brand-orange: #f07020;
    --text-brown: #4a2e12;
    --text-grey: #3c3834;
  }
  * { box-sizing: border-box; margin: 0; padding: 0; }
  html, body {
    width: 1200px; height: 800px; overflow: hidden;
    background: var(--page-bg);
    font-family: "PT Sans", Arial, sans-serif;
  }
  .business-card {
    position: absolute; left: 100px; top: 114px;
    width: 1000px; height: 572px;
    background: linear-gradient(160deg, var(--card-shade) 0%, var(--card-mid) 25%, var(--card-light) 55%, var(--card-mid) 100%);
    box-shadow: 0 12px 30px rgba(0,0,0,0.25);
    overflow: hidden;
  }
  .wave-band { position: absolute; inset: 0; width: 1000px; height: 572px; }
  .contact-person {
    position: absolute; top: 34px; right: 44px;
    text-align: right; color: var(--text-grey);
    font-size: 21px; line-height: 1.3;
  }
  .contact-person .phone { display: inline-flex; align-items: center; gap: 6px; }
  .brand-name {
    position: absolute; top: 150px; left: 0; width: 1000px;
    text-align: center; color: var(--brand-orange);
    font-weight: 700; font-size: 120px; letter-spacing: 1px;
  }
  .contact-address {
    position: absolute; top: 420px; left: 0; width: 1000px;
    text-align: center; color: var(--text-brown);
    font-size: 25px; line-height: 1.55;
  }
  .contact-address p { display: flex; justify-content: center; align-items: center; gap: 8px; }
  .icon { width: 20px; height: 20px; flex: none; }
</style>
</head>
<body>
  <div class="business-card">
    <svg class="wave-band" viewBox="0 0 1000 572" aria-hidden="true">
      <defs>
        <linearGradient id="brownMetal" x1="0" y1="0" x2="1" y2="0">
          <stop offset="0" stop-color="var(--brown-dark)"/>
          <stop offset="0.3" stop-color="var(--brown-mid)"/>
          <stop offset="0.55" stop-color="var(--brown-light)"/>
          <stop offset="0.8" stop-color="var(--brown-mid)"/>
          <stop offset="1" stop-color="var(--brown-dark)"/>
        </linearGradient>
      </defs>
      <path d="M0,500 C140,370 300,350 500,335 C700,318 860,250 1000,130 L1000,572 L0,572 Z" fill="var(--stripe-yellow)"/>
      <path d="M0,510 C140,380 300,360 500,345 C700,328 860,260 1000,140 L1000,572 L0,572 Z" fill="var(--stripe-orange)"/>
      <path d="M0,520 C140,390 300,370 500,355 C700,338 860,270 1000,150 L1000,572 L0,572 Z" fill="url(#brownMetal)"/>
    </svg>

    <div class="contact-person">
      <p class="name">Calvin Obeng</p>
      <p class="role">Director</p>
      <p class="phone">
        <svg class="icon" viewBox="0 0 20 20" aria-hidden="true"><rect x="5" y="2" width="10" height="16" rx="2" fill="none" stroke="currentColor" stroke-width="2"/><circle cx="10" cy="15" r="1" fill="currentColor"/></svg>
        : 00233(0)507318924
      </p>
    </div>

    <h1 class="brand-name">Brightbay</h1>

    <div class="contact-address">
      <p>
        <svg class="icon" viewBox="0 0 20 20" aria-hidden="true"><path d="M10 1a6 6 0 0 0-6 6c0 5 6 12 6 12s6-7 6-12a6 6 0 0 0-6-6z" fill="currentColor"/><circle cx="10" cy="7" r="2.2" fill="var(--brown-light)"/></svg>
        : P.O.Box Dunmore 5172, Accra, Ghana
      </p>
      <p>
        <svg class="icon" viewBox="0 0 20 20" aria-hidden="true"><rect x="1.5" y="4" width="17" height="12" fill="none" stroke="currentColor" stroke-width="1.6"/><path d="M1.5 4l8.5 7 8.5-7" fill="none" stroke="currentColor" stroke-width="1.6"/></svg>
        : calvin.obeng@mailvora.co.uk
      </p>
    </div>
  </div>
</body>
</html>
```